regPersonal Trainer Flyer Design

Reason: I have been very busy with other work and would like to extend the deadline to offer designers the chance to edit and improve designs with my help. Thank you for all the designs that have been sent so far.

```html
<!DOCTYPE html>
<html lang="en">
<head>
<meta charset="utf-8">
<title>Personal Trainer Sam Hollis – Flyer</title>
<link rel="stylesheet" href="https://fonts.googleapis.com/css2?family=Goudy+Bookletter+1911&display=swap">
<style>
  :root {
    --paper: #eef1ef;
    --ink-light: #ffffff;
    --brick-dark: #2a1f1c;
    --brick-mid: #5b3f36;
    --brick-warm: #7a5246;
    --gym-red: #d0202b;
    --gym-red-deep: #9c161e;
    --gym-white: #eceff0;
    --gym-ball: #a9b7b2;
    --bronze-dark: #1b1512;
    --bronze-mid: #4a3a2e;
    --bronze-warm: #8a6d52;
    --grey-1: #2b2d2c;
    --grey-2: #3d3f3e;
    --grey-3: #555756;
    --grey-4: #6e706f;
    --grey-5: #8a8c8b;
  }
  * { margin: 0; padding: 0; box-sizing: border-box; }
  html, body { width: 1200px; height: 900px; overflow: hidden; background: var(--paper); }
  .flyer {
    position: relative; width: 1200px; height: 900px;
    background: var(--paper);
    font-family: "Goudy Bookletter 1911", "Goudy Old Style", Georgia, serif;
    color: var(--ink-light);
  }
  .photo { position: absolute; overflow: hidden; }

  /* left strip of faded gym photos */
  .side-strip { left: 0; top: 120px; width: 108px; height: 667px; }
  .side-strip .tile { position: absolute; left: 0; width: 108px; }
  .side-strip .t1 { top: 0; height: 222px; background: linear-gradient(160deg, var(--grey-4) 0%, var(--grey-2) 55%, var(--grey-1) 100%); }
  .side-strip .t2 { top: 222px; height: 223px; background: linear-gradient(180deg, var(--grey-5) 0%, var(--grey-3) 45%, var(--grey-1) 100%); }
  .side-strip .t3 { top: 445px; height: 222px; background: linear-gradient(200deg, var(--grey-4) 0%, var(--grey-2) 60%, var(--grey-1) 100%); }

  /* left column: three stacked photos */
  .lift-top {
    left: 108px; top: 0; width: 410px; height: 300px;
    background:
      radial-gradient(ellipse 45% 55% at 55% 55%, rgba(30,28,30,.85) 0%, rgba(30,28,30,0) 100%),
      linear-gradient(135deg, var(--brick-warm) 0%, var(--brick-mid) 45%, var(--brick-dark) 100%);
  }
  .suspension-training {
    left: 108px; top: 300px; width: 410px; height: 300px;
    background:
      radial-gradient(ellipse 30% 40% at 12% 45%, var(--gym-ball) 0%, rgba(169,183,178,0) 100%),
      linear-gradient(95deg, var(--gym-white) 0%, #d9dcdc 48%, var(--gym-red) 60%, var(--gym-red) 85%, var(--gym-red-deep) 100%);
  }
  .lift-bottom {
    left: 108px; top: 600px; width: 410px; height: 300px;
    background:
      radial-gradient(ellipse 40% 45% at 40% 35%, var(--bronze-warm) 0%, rgba(138,109,82,0) 100%),
      radial-gradient(ellipse 35% 60% at 82% 60%, #0d0a09 0%, rgba(13,10,9,0) 100%),
      linear-gradient(160deg, var(--bronze-mid) 0%, var(--bronze-dark) 100%);
  }

  /* right panel: greyscale gym collage of six tiles */
  .collage { left: 518px; top: 120px; width: 682px; height: 667px; }
  .collage .tile { position: absolute; }
  .collage .c1 { left: 0; top: 0; width: 282px; height: 222px; background: linear-gradient(170deg, var(--grey-4) 0%, var(--grey-2) 70%, var(--grey-1) 100%); }
  .collage .c2 { left: 282px; top: 0; width: 400px; height: 222px; background: linear-gradient(200deg, var(--grey-5) 0%, var(--grey-3) 55%, var(--grey-2) 100%); }
  .collage .c3 { left: 0; top: 222px; width: 282px; height: 223px; background: linear-gradient(160deg, var(--grey-3) 0%, var(--grey-2) 60%, var(--grey-1) 100%); }
  .collage .c4 { left: 282px; top: 222px; width: 400px; height: 223px; background: radial-gradient(ellipse 50% 60% at 45% 45%, var(--grey-5) 0%, var(--grey-3) 60%, var(--grey-2) 100%); }
  .collage .c5 { left: 0; top: 445px; width: 282px; height: 222px; background: linear-gradient(190deg, var(--grey-4) 0%, var(--grey-2) 55%, var(--grey-1) 100%); }
  .collage .c6 { left: 282px; top: 445px; width: 400px; height: 222px; background: linear-gradient(170deg, var(--grey-5) 0%, var(--grey-3) 60%, var(--grey-2) 100%); }
  .collage-shade {
    position: absolute; left: 518px; top: 120px; width: 682px; height: 667px;
    background: linear-gradient(90deg, rgba(15,15,15,.35) 0%, rgba(15,15,15,.2) 100%);
  }

  .copy { position: absolute; left: 518px; top: 120px; width: 682px; height: 667px; }
  .headline {
    position: absolute; left: 100px; top: 51px;
    font-size: 38px; font-weight: 400; white-space: nowrap;
  }
  .prompts { position: absolute; left: 39px; top: 161px; list-style: none; }
  .prompts li {
    position: relative; padding-left: 21px; height: 50.3px;
    font-size: 20.5px; line-height: 24px; white-space: nowrap;
  }
  .prompts li::before {
    content: ""; position: absolute; left: 0; top: 10px;
    width: 5px; height: 5px; border-radius: 50%; background: var(--ink-light);
  }
  .offer {
    position: absolute; left: 132px; top: 554px;
    font-size: 24px; white-space: nowrap;
  }
  .contact {
    position: absolute; left: 74px; top: 600px;
    font-size: 19px; white-space: nowrap;
  }
  .contact span + span { margin-left: 22px; }
</style>
</head>
<body>
<main class="flyer">
  <div class="photo side-strip" role="img" aria-label="Faded greyscale gym photos of the trainer with clients">
    <div class="tile t1"></div><div class="tile t2"></div><div class="tile t3"></div>
  </div>
  <div class="photo lift-top" role="img" aria-label="Trainer performing a barbell squat against a brick wall"></div>
  <div class="photo suspension-training" role="img" aria-label="Trainer coaching a client on suspension straps in a red and white gym"></div>
  <div class="photo lift-bottom" role="img" aria-label="Trainer lifting a barbell with weight plates, close up"></div>
  <div class="photo collage" role="img" aria-label="Greyscale collage of the trainer coaching clients with gym equipment">
    <div class="tile c1"></div><div class="tile c2"></div><div class="tile c3"></div>
    <div class="tile c4"></div><div class="tile c5"></div><div class="tile c6"></div>
  </div>
  <div class="collage-shade"></div>

  <section class="copy">
    <h1 class="headline">Personal Trainer Sam Hollis</h1>
    <ul class="prompts">
      <li>“Lacking motivation?”</li>
      <li>“Not achieving your goals?”</li>
      <li>“Need help?”</li>
      <li>“Bored of the gym?”</li>
      <li>“You're never too old”</li>
      <li>“I can help improve your health and well-being”</li>
      <li>“Training can be at your home”</li>
    </ul>
    <p class="offer">*Introductory offer – one free session*</p>
    <p class="contact"><span>Tel - 07700900461</span><span>Email - samhollis.pt@mailbox.co.uk</span></p>
  </section>
</main>
</body>
</html>
```